Flyer-Design für Amerikanische Chiropraktik
Zielgruppe
Praxis für Amerikanische Chiropraktik
Zielgruppe: Gesundheitsbewusste Menschen, gerne gebildet, Affinität zu Sport/Yoga etc.
Flyer soll modern und hochwertig sein (Zielgruppe auch Privatversicherte und Büroleute)
Aufgabenstellung
Bitte keine Schnörkel.
Klare Linien. Straight einfach
Positive Vibes
Website ist nicht final fertig. Das blau/grau und das Grün wird aber aller Voraussicht nach Weiter verwendet. Falls das rot verwendet wird eher nicht so oft bitte.
Sehr gerne für die Überschriften die gleichen Balken unter den Überschriften für den Flyer verwenden.
Flyer bei Nordra Druck ist 99x210 mm (ich denke mit etwas Spiel am Rand für den Druck.) 6 Seiten.
Auf der letzten Seite (sollte die mittlere Rückseite sein) bitte Kontaktdaten und evtl Portraitbild.

```html
<!DOCTYPE html>
<html lang="de">
<head>
<meta charset="utf-8">
<title>Flyer Chiropraktik Kasimir Holt</title>
<link rel="stylesheet" href="https://fonts.googleapis.com/css2?family=Poppins:ital,wght@0,400;0,600;0,700;1,700&family=Open+Sans:wght@400;600&display=swap">
<style>
:root{
  --gold:#b3a276;
  --gold-text:#b9a070;
  --dark:#2b2a2d;
  --white:#ffffff;
  --ink:#1f1e20;
  --page:#e9e9ea;
  --photo-warm:#cdb9a4;
  --photo-light:#e6ddd3;
  --photo-grey:#8d8b8a;
}
*{box-sizing:border-box;margin:0;padding:0}
html,body{width:909px;height:1200px;overflow:hidden;background:var(--page)}
body{font-family:"Open Sans",Arial,sans-serif;color:var(--ink);position:relative}
.sheet{position:absolute;left:55px;width:798px;height:565px;display:grid;grid-template-columns:repeat(3,1fr);box-shadow:0 6px 18px rgba(0,0,0,.18)}
.sheet--outside{top:20px}
.sheet--inside{top:615px}
.panel{position:relative;overflow:hidden}
.panel--dark{background:var(--dark);color:var(--white)}
.panel--gold{background:var(--gold)}
.panel--white{background:var(--white)}
.photo{position:absolute;left:0;right:0}
.photo--chevron{clip-path:polygon(0 0,100% 0,100% 82%,50% 100%,0 82%)}
.headline{font-family:"Poppins",Arial,sans-serif}
.accent{color:var(--gold-text)}
.brand{display:flex;align-items:center;justify-content:center;gap:6px;font-family:"Poppins",Arial,sans-serif;font-weight:400;font-size:10px;letter-spacing:1.5px;text-transform:uppercase;color:var(--dark)}
.brand__dot{width:14px;height:14px;border:1.5px solid currentColor;border-radius:50%;flex:none}
.brand--light{color:var(--white)}

/* flap */
.flap__photo{top:0;height:150px;background:linear-gradient(135deg,var(--photo-light),var(--photo-grey) 60%,#5b544e)}
.flap__band{position:absolute;top:0;left:0;right:0;height:156px;background:var(--gold);clip-path:polygon(0 0,100% 0,100% 82%,50% 100%,0 82%)}
.flap__body{position:absolute;top:176px;left:22px;right:20px}
.flap__title{font-family:"Poppins",Arial,sans-serif;font-weight:600;font-size:13px;margin-bottom:4px}
.bar{display:block;width:48px;height:2px;background:var(--gold);margin:4px 0 9px}
.flap__text{font-size:8px;line-height:1.5}
.flap__sub{font-family:"Poppins",Arial,sans-serif;font-weight:600;font-size:11px;margin:16px 0 8px}
.flap__list{list-style:none;font-size:8.5px;line-height:2.2}
.flap__list li::before{content:"";display:inline-block;width:5px;height:5px;background:var(--gold);margin-right:8px;vertical-align:middle}

/* back */
.back__points{list-style:none;padding:26px 22px 0 22px}
.back__points li{display:flex;gap:9px;font-size:8px;line-height:1.45;margin-bottom:10px}
.back__points li::before{content:"";flex:none;width:11px;height:11px;border:1.3px solid var(--gold);border-radius:50%;margin-top:1px}
.back__rule{height:2px;background:var(--gold);margin:4px 30px 16px}
.contact{text-align:center;font-size:8.5px;line-height:1.75}
.contact__name{font-family:"Poppins",Arial,sans-serif;font-weight:700;color:var(--gold-text);font-size:10.5px}
.contact__web{color:var(--gold-text);font-weight:600}
.back__hello{text-align:center;font-family:"Poppins",Arial,sans-serif;font-weight:700;color:var(--gold-text);font-size:13px;line-height:1.25;margin-top:20px;padding-right:70px}
.back__brand{position:absolute;left:14px;bottom:64px;width:118px;font-size:8px;letter-spacing:1px}
.back__portrait{position:absolute;right:10px;bottom:0;width:128px;height:165px;background:linear-gradient(180deg,#3a3837,#d9cfc7 45%,#b8c0cc)}

/* cover */
.cover .brand{position:absolute;top:42px;left:0;right:0}
.cover__photo{top:88px;height:255px;left:18px;right:18px;background:linear-gradient(160deg,var(--photo-light),var(--photo-warm) 55%,#d8c6c6)}
.cover__dark{position:absolute;left:0;right:0;bottom:0;height:232px;background:var(--dark);clip-path:polygon(0 0,50% 12%,100% 0,100% 100%,0 100%)}
.cover__text{position:absolute;left:0;right:0;bottom:30px;text-align:center;color:var(--white)}
.cover__lead{font-family:"Poppins",Arial,sans-serif;font-weight:400;font-size:19px;line-height:1.2}
.cover__big{font-family:"Poppins",Arial,sans-serif;font-weight:700;font-size:22px;line-height:1.2}
.cover__claim{font-family:"Poppins",Arial,sans-serif;font-weight:600;font-size:10px;color:var(--gold-text);margin-top:12px;letter-spacing:.3px}

/* inside */
.foot{position:absolute;left:0;right:0;bottom:0;height:40px;background:var(--gold);display:flex;align-items:center;justify-content:center;font-family:"Poppins",Arial,sans-serif;font-weight:700;font-style:italic;color:var(--white);font-size:11px;gap:10px}
.foot__line{width:44px;height:2px;background:var(--white)}
.copy{padding:22px 20px 0 22px}
.copy__title{font-family:"Poppins",Arial,sans-serif;font-weight:700;font-size:10.5px;line-height:1.3}
.copy__text{font-size:7.4px;line-height:1.5;margin-bottom:7px}
.copy__hl{color:var(--gold-text);font-weight:600}
.mid__photo{top:0;height:128px;background:linear-gradient(135deg,#f1ece6,var(--photo-light) 50%,#cfc4b8)}
.mid__body{position:absolute;top:136px;left:20px;right:18px}
.mid__title{font-family:"Poppins",Arial,sans-serif;font-weight:600;font-size:10.5px;color:var(--white)}
.mid__text{font-size:7.4px;line-height:1.5;margin-bottom:14px}
.cause{display:flex;gap:12px;margin-bottom:14px;align-items:flex-start}
.cause__icon{flex:none;width:30px;height:30px;border:1.3px solid var(--white);border-radius:6px;opacity:.85}
.cause__name{font-family:"Poppins",Arial,sans-serif;font-weight:600;font-size:9.5px;color:var(--gold-text)}
.cause__text{font-size:7.6px;line-height:1.45}
.right__photo{top:258px;bottom:40px;background:linear-gradient(180deg,#e9e3dc,var(--photo-warm) 55%,#c9a987)}
.right__copy{padding:20px 16px 0 18px}
</style>
</head>
<body>

<section class="sheet sheet--outside" aria-label="Außenseite">
  <!-- inner flap -->
  <article class="panel panel--dark flap">
    <div class="flap__band"></div>
    <div class="photo photo--chevron flap__photo" role="img" aria-label="Foto einer Chiropraktik-Liege mit Justiergerät"></div>
    <div class="flap__body">
      <h2 class="flap__title">Was behandeln wir?</h2>
      <span class="bar"></span>
      <p class="flap__text">Die Amerikanische Chiropraktik verfolgt einen ganzheitlichen und ursachenbezogenen Ansatz, wodurch sich vielseitige Anwendungsbereiche ergeben. Das Angebot reicht von Gesundheitsvorsorge bis zur Behandlung von bereits existierenden Beschwerden und Symptomen.</p>
      <h3 class="flap__sub">Wir helfen uns Menschen mit:</h3>
      <ul class="flap__list">
        <li>Rückenschmerzen</li>
        <li>Nackenverspannungen</li>
        <li>Kopfschmerzen und Migräne</li>
        <li>Gelenkschmerzen</li>
        <li>Schlafproblemen</li>
        <li>Kribbeln in Händen oder Füßen</li>
      </ul>
    </div>
  </article>

  <!-- back panel -->
  <article class="panel panel--dark back">
    <ul class="back__points">
      <li>Wir sind Experten auf unserem Gebiet.</li>
      <li>Arbeiten nach neuesten Wissenschaftlichen Kenntnissen. Sanfte und zielgerichtete Behandlung.</li>
      <li>Profitieren Sie von langjährige praktische Erfahrung und modernen neurowissenschaftliche Aspekten in der chiropraktischen Behandlung.</li>
      <li>Wir sind mit Freude und Engagement für Dich und Deine Gesundheit da.</li>
    </ul>
    <div class="back__rule"></div>
    <address class="contact" style="font-style:normal">
      <div class="contact__name">Kasimir Holt</div>
      <div>Heil- und Chiropraktiker,<br>B.Sc. Physiotherapie</div>
      <div style="margin-top:6px">Lindenweg 12 | 83999 Bergau</div>
      <div>Tel: 0151/2345678</div>
      <div>praxis@chiropraktik-holt.de</div>
      <div class="contact__web">www.chiropraktik-holt.de</div>
    </address>
    <p class="back__hello">Wir freuen uns<br>auf Dich!</p>
    <div class="brand brand--light back__brand"><span class="brand__dot"></span><span>Chiropraktik Kasimir Holt</span></div>
    <div class="back__portrait" role="img" aria-label="Portraitfoto des Chiropraktikers, sitzend im weißen T-Shirt"></div>
  </article>

  <!-- cover -->
  <article class="panel panel--gold cover">
    <div class="brand"><span class="brand__dot"></span><span>Chiropraktik Kasimir Holt</span></div>
    <div class="cover__dark"></div>
    <div class="photo photo--chevron cover__photo" role="img" aria-label="Foto: Chiropraktiker umarmt eine Patientin"></div>
    <div class="cover__text">
      <p class="cover__lead">Ihr weg zu mehr</p>
      <p class="cover__big">Wohlbefinden</p>
      <p class="cover__claim">MODERN.URSÄCHLICH.ANDERS.</p>
    </div>
  </article>
</section>

<section class="sheet sheet--inside" aria-label="Innenseite">
  <article class="panel panel--white">
    <div class="copy">
      <h2 class="copy__title">Was ist <span class="accent">Amerikanische Chiropraktik?</span></h2>
      <span class="bar"></span>
      <p class="copy__text">Amerikanische Chiropraktik ist eine eigenständige, ganzheitliche und vitalistische Form der Gesundheitspflege, die darauf ausgerichtet ist, Gesundheit und Funktion des menschlichen Körpers wiederherzustellen und zu erhalten.</p>
      <p class="copy__text">Sie ist sowohl eine evidenzbasierte Wissenschaft als auch eine Heilkunst und eine Philosophie, die nach der optimalen Funktion des Nervensystems strebt.</p>
      <h2 class="copy__title" style="margin-top:12px">Wie funktioniert <span class="accent">Chiropraktik?</span></h2>
      <span class="bar"></span>
      <p class="copy__text">Der Körper wird von seinem Nervensystem gesteuert. Es ist dafür verantwortlich, wie ein Mensch seine Umwelt wahrnimmt und durch das Leben geht. Über das Nervensystem empfängt und sendet das Gehirn fortwährend Informationen an Organe, Muskeln und alle anderen Strukturen. Seine optimale Funktion ist demnach von größter Bedeutung.</p>
      <p class="copy__text">Im besten Fall werden Körper und Psyche über das Nervensystem in Balance gehalten. Dazu muss alles störungsfrei miteinander vernetzt sein. Fehlstellungen und Blockaden können die Vernetzung stören: Es kommt zu sogenannten Subluxationen. Das physische und psychische Gleichgewicht gerät ins Wanken. Die Folgen können sehr vielfältig sein. Muskelverspannungen, Nackenschmerzen, Kopfschmerzen oder Rückenschmerzen können die Folge sein. Oft bleiben solche <span class="copy__hl">Subluxationen</span> über Jahre unbemerkt, bevor sie Schmerzen und/oder psycho-emotionale Symptome verursachen.</p>
    </div>
    <div class="foot"><span class="foot__line"></span><span>"Time to Connect Your Brain."</span></div>
  </article>

  <article class="panel panel--dark">
    <div class="photo mid__photo" role="img" aria-label="Foto einer chiropraktischen Behandlung am Oberkörper"></div>
    <div class="mid__body">
      <h2 class="mid__title">Was ist eigentlich eine <span class="accent">Subluxation?</span></h2>
      <span class="bar"></span>
      <p class="mid__text">Wir definieren eine vertebrale Subluxation als ein dysfunktionales Gebiet in der Wirbelsäule, dass sich aufgrund seines Einflusses auf das Nervensystem negativ auf die Gesundheit und das Wohlbefinden auswirkt. Die Funktion der Wirbelsäule als wichtiger Informationsgeber für das Gehirn ist gestört.</p>
      <h2 class="mid__title" style="margin-bottom:12px">Ursachen für eine <span class="accent">Subluxation</span></h2>
      <div class="cause">
        <div class="cause__icon" role="img" aria-label="Symbol für physischen Stress"></div>
        <div><div class="cause__name">Physischer Stress</div><p class="cause__text">wie z.B. Trauma (Brüche etc.) Unfälle, langes Sitzen, Bewegungsmangel</p></div>
      </div>
      <div class="cause">
        <div class="cause__icon" role="img" aria-label="Symbol für toxischen Stress"></div>
        <div><div class="cause__name">Toxischer Stress</div><p class="cause__text">wie z.B. Zigaretten, Alkohol, Drogen, Abgase, Medikamente, Übersäuerung</p></div>
      </div>
      <div class="cause">
        <div class="cause__icon" role="img" aria-label="Symbol für psychischen Stress"></div>
        <div><div class="cause__name">Psychischer Stress</div><p class="cause__text">Macht einen großen Anteil aus. Druck und hohe Anforderungen im Beruf, Alltagsstress, Schlafmangel, Sorgen, Überforderung.</p></div>
      </div>
    </div>
    <div class="foot" style="font-size:10.5px">www.chiropraktik-holt.de</div>
  </article>

  <article class="panel panel--white">
    <div class="right__copy">
      <h2 class="copy__title">Wie helfen wir? <span class="accent">Die Justierung</span></h2>
      <span class="bar"></span>
      <p class="copy__text">Die chiropraktische Justierung korrigiert eine Subluxation, indem sie das schadhafte neurologische Muster durchbricht. Durch einen sanften und gezielten Impuls wird die physiologische Beweglichkeit und Position eines Gelenkes wieder hergestellt und faszialer Adhäsionen gelöst. Die Impulse führen zu einer messbaren Verbesserung in der Funktion hinsichtlich der Beziehung zwischen Nervensystem und Bewegungsapparat (Lindqvist et al., 2021). Der chiropraktische Impuls wirkt auf struktureller Ebene (am Gelenk) und im Nervensystem. Der Informationsfluss zwischen Körper und Nervensystem wird harmonisiert und Selbstheilungskräfte aktiviert, um dir eine volle Funktionalität und mehr Lebensqualität zu ermöglichen.</p>
    </div>
    <div class="photo right__photo" role="img" aria-label="Foto: Chiropraktiker justiert den Rücken einer liegenden Patientin"></div>
    <div class="foot"><span>"Time to Connect Your Brain."</span><span class="foot__line"></span></div>
  </article>
</section>

</body>
</html>
```